Brightmoor Notes To Do List

I am looking to design a new "Study To Do List" for High School students (Ages 15 - 18) . This will be printed as an A4 notepad and so should only be a single A4 page.

The Design will need to be professional and look semi-serious but also be appealing to High school students (Ages 15 - 18) and should NOT be gender specific.

I have attached a word document outlining the structure of the page. The space provided should be large enough that people can write in it comfortably.

The notepad will most likely be printed in black and white but I'm also looking at coloured options - colours should be kept to a minimum.

This will be printed professionally and should also include a 3mm bleed.

The design should also include the business logo (included in the word document)

Target Market(s)

High School students (Ages 15 - 18). Both genders

Industry/Entity Type

Education

Font styles to use
Serif
Sans Serif

Requirements
Must have
• Please see the word document attached.
Should not have
• Too much colour

```html
<!DOCTYPE html>
<html lang="en">
<head>
<meta charset="utf-8">
<title>Brightmoor Notes – Study To Do List</title>
<link href="https://fonts.googleapis.com/css2?family=Roboto:wght@400;700;900&family=Roboto+Condensed:wght@700&display=swap" rel="stylesheet">
<style>
  :root{
    --navy:#1d3045;
    --orange:#ff7300;
    --charcoal:#2b2b2b;
    --grey:#a5a5a5;
    --stripe:#ececec;
    --cell:#e6e6e6;
    --paper:#ffffff;
  }
  html,body{margin:0;padding:0;width:1200px;height:960px;overflow:hidden;background:#ffffff;}
  .stage{position:relative;width:1200px;height:960px;}
  .sheet{position:absolute;top:112px;width:529px;height:741px;box-shadow:0 0 0 1px #e4e4e4;}
  .sheet--colour{left:47px;--dark:var(--navy);--accent:var(--orange);}
  .sheet--mono{left:612px;--dark:var(--charcoal);--accent:var(--grey);}
  .sheet svg{display:block;width:529px;height:741px;}
  .label{font-family:"Roboto",Arial,sans-serif;font-weight:700;}
  .date-label{font-family:"Roboto",Arial,sans-serif;font-weight:900;font-size:19px;}
  .brand{font-family:"Roboto",Arial,sans-serif;font-weight:900;font-size:23px;}
  .web{font-family:"Roboto Condensed","Arial Narrow",sans-serif;font-weight:700;font-size:17px;}
</style>
</head>
<body>
<div class="stage">

  <div class="sheet sheet--colour">
    <svg viewBox="0 0 661 926" xmlns="http://www.w3.org/2000/svg">
      <defs>
        <symbol id="study-sheet" viewBox="0 0 661 926">
          <rect width="661" height="926" fill="#fff"/>
          <!-- header bands -->
          <rect x="0" y="0" width="320" height="28" style="fill:var(--dark)"/>
          <polygon points="212,0 661,0 661,60 313,60" style="fill:var(--accent)"/>
          <rect x="333" y="24" width="215" height="25" fill="#d0d0d0"/>
          <rect x="331" y="22" width="215" height="25" fill="#fff"/>
          <text class="date-label" x="561" y="44" style="fill:var(--dark)">DATE:</text>

          <!-- brand -->
          <circle cx="62" cy="110" r="16" style="fill:var(--accent)"/>
          <text class="brand" x="86" y="104" style="fill:var(--dark)">Brightmoor</text>
          <text class="brand" x="86" y="130" style="fill:var(--dark)">Notes</text>

          <!-- commitments / to do -->
          <rect x="217" y="105" width="394" height="26" style="fill:var(--dark)"/>
          <line x1="414" y1="105" x2="414" y2="131" stroke="#fff" stroke-width="1.5"/>
          <text class="label" x="307" y="122" font-size="8.5" fill="#fff" text-anchor="middle" letter-spacing=".4">COMMITMENTS</text>
          <text class="label" x="500" y="122" font-size="8.5" fill="#fff" text-anchor="middle" letter-spacing=".8">TO DO</text>
          <g fill="var(--cell)" style="fill:var(--cell)">
            <rect x="217" y="131" width="14" height="116"/>
            <rect x="414" y="131" width="14" height="116"/>
          </g>
          <g stroke="#555" stroke-width="1" fill="none">
            <rect x="217" y="131" width="394" height="116"/>
            <line x1="414" y1="131" x2="414" y2="247"/>
            <line x1="217" y1="154" x2="611" y2="154"/>
            <line x1="217" y1="177" x2="611" y2="177"/>
            <line x1="217" y1="201" x2="611" y2="201"/>
            <line x1="217" y1="224" x2="611" y2="224"/>
          </g>
          <g class="label" font-size="8" fill="#222">
            <text x="222" y="145">1</text><text x="419" y="145">1</text>
            <text x="222" y="168">2</text><text x="419" y="168">2</text>
            <text x="222" y="191">3</text><text x="419" y="191">3</text>
            <text x="222" y="215">4</text><text x="419" y="215">4</text>
            <text x="222" y="238">5</text><text x="419" y="238">5</text>
          </g>

          <!-- reminders -->
          <rect x="50" y="266" width="64" height="12" style="fill:var(--dark)"/>
          <text class="label" x="54" y="275" font-size="8" fill="#fff">REMINDERS</text>
          <g style="fill:var(--stripe)">
            <rect x="52" y="281" width="558" height="18"/>
            <rect x="52" y="328" width="558" height="18"/>
            <rect x="52" y="376" width="558" height="18"/>
          </g>
          <rect x="50" y="278" width="562" height="147" fill="none" stroke="#555" stroke-width="1"/>

          <!-- notes -->
          <rect x="50" y="448" width="60" height="18" style="fill:var(--dark)"/>
          <text class="label" x="57" y="461" font-size="9.5" fill="#fff" font-weight="400">NOTES:</text>
          <rect x="50" y="466" width="20" height="385" style="fill:var(--dark)"/>
          <rect x="50" y="466" width="562" height="385" fill="none" stroke="var(--dark)" style="stroke:var(--dark)" stroke-width="1.2"/>
          <g style="stroke:var(--dark)" stroke-width="1">
            <line x1="50" y1="489" x2="612" y2="489"/><line x1="50" y1="511" x2="612" y2="511"/>
            <line x1="50" y1="534" x2="612" y2="534"/><line x1="50" y1="557" x2="612" y2="557"/>
            <line x1="50" y1="579" x2="612" y2="579"/><line x1="50" y1="602" x2="612" y2="602"/>
            <line x1="50" y1="625" x2="612" y2="625"/><line x1="50" y1="647" x2="612" y2="647"/>
            <line x1="50" y1="670" x2="612" y2="670"/><line x1="50" y1="693" x2="612" y2="693"/>
            <line x1="50" y1="715" x2="612" y2="715"/><line x1="50" y1="738" x2="612" y2="738"/>
            <line x1="50" y1="761" x2="612" y2="761"/><line x1="50" y1="783" x2="612" y2="783"/>
            <line x1="50" y1="806" x2="612" y2="806"/><line x1="50" y1="829" x2="612" y2="829"/>
          </g>
          <g class="label" font-size="8" fill="#fff">
            <text x="55" y="480">1</text><text x="55" y="503">2</text><text x="55" y="526">3</text>
            <text x="55" y="549">4</text><text x="55" y="571">5</text><text x="55" y="594">6</text>
            <text x="55" y="617">7</text><text x="55" y="639">8</text><text x="55" y="662">9</text>
            <text x="54" y="685">10</text><text x="54" y="707">11</text><text x="54" y="730">12</text>
            <text x="54" y="753">13</text><text x="54" y="775">14</text><text x="54" y="798">15</text>
            <text x="54" y="821">16</text><text x="54" y="843">17</text>
          </g>

          <!-- footer bands -->
          <polygon points="333,888 343,888 318,905 661,905 661,926 263,926" style="fill:var(--dark)"/>
          <polygon points="0,888 326,888 275,926 0,926" style="fill:var(--accent)"/>
          <text class="web" x="32" y="913" fill="#fff">www.brightmoornotes.com.au</text>
        </symbol>
      </defs>
      <use href="#study-sheet" x="0" y="0" width="661" height="926"/>
    </svg>
  </div>

  <div class="sheet sheet--mono">
    <svg viewBox="0 0 661 926" xmlns="http://www.w3.org/2000/svg">
      <use href="#study-sheet" x="0" y="0" width="661" height="926"/>
    </svg>
  </div>

</div>
</body>
</html>
```